Criação de Papelaria Profissional para Advocacia e Direito
A empresa queria:
" Ribeiro Tavares Advogados é um escritório boutique de atuação diversificada (full service) "

```html
<!DOCTYPE html>
<html lang="pt-BR">
<head>
<meta charset="UTF-8">
<title>Ribeiro Tavares Advogados – Papel Timbrado</title>
<link href="https://fonts.googleapis.com/css2?family=Montserrat:wght@300;400;500&display=swap" rel="stylesheet">
<style>
  :root {
    --brand: #1f5570;
    --brand-dark: #184660;
    --paper: #ffffff;
    --backdrop: #e9e7e3;
    --ink: #3a3a3a;
    --rule: #c9ced2;
    --ghost: #e6e6e6;
  }
  * { margin: 0; padding: 0; box-sizing: border-box; }
  html, body {
    width: 1200px; height: 1200px; overflow: hidden;
    background: var(--backdrop);
    font-family: "Montserrat", sans-serif;
  }
  .letterhead {
    position: absolute; left: 210px; top: 46px;
    width: 780px; height: 1104px;
    background: var(--paper);
    box-shadow: 0 6px 18px rgba(0,0,0,.18);
    overflow: hidden;
  }
  .letterhead__header {
    height: 144px; background: var(--brand);
    display: flex; flex-direction: column; align-items: center; justify-content: center;
    color: #fff;
  }
  .brand__mark {
    width: 30px; height: 30px; border: 2px solid #fff; margin-bottom: 8px;
  }
  .brand__name {
    font-weight: 400; font-size: 27px; letter-spacing: 3px; text-transform: uppercase;
  }
  .brand__tagline {
    font-weight: 300; font-size: 8px; letter-spacing: 2.5px; text-transform: uppercase;
    margin-top: 5px; opacity: .85;
  }
  .letterhead__emblem {
    position: absolute; left: 282px; top: 437px;
    width: 216px; height: 216px;
    border: 6px solid var(--ghost);
  }
  .letterhead__rule {
    position: absolute; left: 0; right: 0; top: 1030px;
    height: 1px; background: var(--rule);
  }
  .letterhead__rule-accent {
    position: absolute; left: 570px; width: 170px; top: 1028px;
    height: 4px; background: var(--brand);
  }
  .contact {
    position: absolute; left: 0; right: 0; top: 1050px;
    display: flex; justify-content: space-between; align-items: center;
    padding: 0 40px 0 34px;
    font-size: 14px; color: var(--ink);
  }
  .contact__item { display: flex; align-items: center; gap: 10px; }
  .contact__icon { width: 20px; height: 20px; fill: none; stroke: var(--ink); stroke-width: 1.8; }
  .contact__square { width: 16px; height: 16px; border: 1.8px solid var(--ink); }
  .letterhead__footer-band {
    position: absolute; left: 0; right: 0; bottom: 0; height: 12px; background: var(--brand-dark);
  }
</style>
</head>
<body>
  <main class="letterhead">
    <header class="letterhead__header">
      <div class="brand__mark"></div>
      <div class="brand__name">Ribeiro Tavares</div>
      <div class="brand__tagline">Advogados e Consultores</div>
    </header>

    <div class="letterhead__emblem"></div>

    <div class="letterhead__rule"></div>
    <div class="letterhead__rule-accent"></div>

    <footer class="contact">
      <div class="contact__item">
        <svg class="contact__icon" viewBox="0 0 24 24"><path d="M5 3h4l2 5-2.5 1.5a11 11 0 0 0 6 6L16 13l5 2v4a2 2 0 0 1-2 2A16 16 0 0 1 3 5a2 2 0 0 1 2-2z"/></svg>
        <span>00 0000-0000 | 00 00000-0000</span>
      </div>
      <div class="contact__item">
        <svg class="contact__icon" viewBox="0 0 24 24"><rect x="3" y="5" width="18" height="14"/><path d="M3 5l9 8 9-8"/></svg>
        <span>contato@ribeirotavares.adv.br</span>
      </div>
      <div class="contact__item">
        <div class="contact__square"></div>
        <span>ribeirotavares.adv</span>
      </div>
    </footer>

    <div class="letterhead__footer-band"></div>
  </main>
</body>
</html>
```